Candle Box & Belly Band Design

Design Candle Box for Soy Candles along with a belly band design that can be used on off the shelf coloured boxes. It is for a premium brand of candle - so i want the packaging to reflect this. I have included must haves below.

The candle boxes will be a few different sizes, but for the purpose of the design it would be something like a cube 12 x 12 x 12 cms

The belly band for standard boxes to be something like 5cm wide on a 12 x 12 x 12cms cube box that goes all the way around the top to the bottom - holding the lid on and providing all the relevant information. Example of box with belly band uploaded

Our company Name : Hazel & Pip - our logo is uploaded

Target Market(s)

Premium Candle Buyers

Colors

Designer to choose colors to be used in the design.

Requirements
Must have
• Must have our logo - our logo can be in any colour
• Must state:
• Soy Candle, Hand Poured, Made in Melbourne,
• A space for the fragrance, size and burn time.
• For this project use Lime, Coconut & Elderfllower, 300grams, 50 Hour burn Time

```html
<!DOCTYPE html>
<html lang="en">
<head>
<meta charset="utf-8">
<title>Hazel &amp; Pip Soy Candle Box</title>
<link rel="stylesheet" href="https://fonts.googleapis.com/css2?family=Libre+Baskerville&family=Ubuntu:wght@400&family=Arimo:wght@400&family=Cousine&display=swap">
<style>
  :root {
    --backdrop: #d9d7ef;
    --box-face: #f7f4f8;
    --box-edge: #ece7ef;
    --band: #201818;
    --accent: #e1247b;
    --ink-light: #ffffff;
    --ink-soft: #e9e4e4;
  }
  html, body {
    margin: 0;
    padding: 0;
    width: 1200px;
    height: 1076px;
    overflow: hidden;
    background: var(--backdrop);
  }
  .canvas {
    position: relative;
    width: 1200px;
    height: 1076px;
  }
  .box-front {
    position: absolute;
    left: 275px;
    top: 255px;
    width: 575px;
    height: 728px;
    background: linear-gradient(90deg, var(--box-face) 0%, #ffffff 50%, var(--box-edge) 100%);
  }
  .belly-band {
    position: absolute;
    left: 135px;
    top: 0;
    width: 288px;
    height: 728px;
    background: var(--band);
    color: var(--ink-light);
    text-align: center;
  }
  .brand {
    position: absolute;
    top: 66px;
    left: 0;
    width: 100%;
  }
  .brand-dot {
    display: block;
    margin: 0 auto;
    width: 86px;
    height: 86px;
  }
  .brand-name {
    margin: 44px 0 0;
    font-family: "Ubuntu", sans-serif;
    font-size: 30px;
    font-weight: 400;
    color: var(--accent);
    letter-spacing: 0.5px;
  }
  .product-title {
    position: absolute;
    top: 292px;
    left: 0;
    width: 100%;
    margin: 0;
    font-family: "Libre Baskerville", serif;
    font-weight: 400;
    font-size: 50px;
    line-height: 60px;
    color: var(--ink-light);
  }
  .divider-dots {
    position: absolute;
    top: 484px;
    left: 97px;
    width: 96px;
    border-top: 2px dotted var(--ink-soft);
  }
  .method {
    position: absolute;
    top: 504px;
    left: 0;
    width: 100%;
    margin: 0;
    font-family: "Arimo", sans-serif;
    font-size: 16px;
    letter-spacing: 1.5px;
    color: var(--ink-soft);
  }
  .fragrance {
    position: absolute;
    top: 530px;
    left: 0;
    width: 100%;
    margin: 0;
    font-family: "Cousine", monospace;
    font-size: 15.5px;
    line-height: 24px;
    color: var(--accent);
  }
  .spec-row {
    position: absolute;
    top: 613px;
    left: 10px;
    width: 268px;
    display: flex;
    justify-content: space-between;
  }
  .spec {
    flex: 1;
    font-family: "Arimo", sans-serif;
    font-size: 13px;
    line-height: 17px;
    letter-spacing: 0.8px;
    color: var(--ink-light);
    text-transform: uppercase;
  }
  .spec + .spec {
    border-left: 1.5px solid var(--ink-soft);
  }
</style>
</head>
<body>
  <main class="canvas">
    <section class="box-front">
      <div class="belly-band">
        <div class="brand">
          <svg class="brand-dot" viewBox="0 0 86 86" aria-hidden="true">
            <circle cx="43" cy="43" r="43" fill="#e1247b"/>
          </svg>
          <p class="brand-name">Hazel &amp; Pip</p>
        </div>
        <h1 class="product-title">Soy<br>Candle</h1>
        <div class="divider-dots"></div>
        <p class="method">Hand Poured</p>
        <p class="fragrance">Lime, Coconut &amp;<br>Elderflower</p>
        <div class="spec-row">
          <div class="spec">300<br>Grams</div>
          <div class="spec">Made in<br>Melbourne</div>
          <div class="spec">50 Hour<br>Burn Time</div>
        </div>
      </div>
    </section>
  </main>
</body>
</html>
```